Pelverhook LLC
Business Cards & Stationary
Professional
Tobias Wendell
President
482 Orchard Crest Road
Dunmore Falls, NJ 07934-2718
tobias.wendell@mailvexo.com
www.pelverhook.com
I require the full suite of stationary products i.e.:- Business card, letterhead, envelope, fax cover sheet, thank you cards, invoice etc.
Just the logo on the back of the card.

```html
<!DOCTYPE html>
<html lang="en">
<head>
<meta charset="utf-8">
<title>Pelverhook LLC — Business Card</title>
<link rel="stylesheet" href="https://fonts.googleapis.com/css2?family=Marcellus+SC&display=swap">
<style>
  :root {
    --backdrop: #3b3a38;
    --card-light: #ffffff;
    --card-mid: #e9eaec;
    --card-dark: #c9cbcf;
    --band-start: #3f9ad8;
    --band-end: #2c2d8f;
    --band-rule: #1b1c3a;
    --brand-blue: #1f5e9c;
    --ink: #2b2b2b;
    --white: #ffffff;
  }
  * { box-sizing: border-box; margin: 0; padding: 0; }
  html, body {
    width: 1200px; height: 919px; overflow: hidden;
    background: var(--backdrop);
  }
  .stage { position: relative; width: 1200px; height: 919px; }

  .card {
    position: absolute;
    width: 720px; height: 404px;
    border-radius: 22px;
    overflow: hidden;
    background: linear-gradient(160deg, var(--card-light) 0%, var(--card-mid) 55%, var(--card-dark) 100%);
    box-shadow: 0 10px 28px rgba(0,0,0,.35);
  }
  .card--front { left: 40px; top: 40px; }
  .card--back  { left: 440px; top: 475px; }

  .title-band {
    position: absolute; left: 0; top: 0; width: 100%; height: 112px;
    background: linear-gradient(90deg, var(--band-start) 0%, #3470c4 45%, var(--band-end) 100%);
    border-bottom: 5px solid var(--band-rule);
  }
  .title-band__name, .title-band__role {
    position: absolute; left: 392px;
    font-family: "Marcellus SC", serif; color: var(--white);
    letter-spacing: .5px;
  }
  .title-band__name { top: 34px; font-size: 25px; }
  .title-band__role { top: 66px; font-size: 19px; letter-spacing: 1px; }

  .brand {
    position: absolute; display: flex; flex-direction: column; align-items: center;
  }
  .brand__mark {
    border-radius: 50%;
    background: var(--brand-blue);
  }
  .brand__name {
    font-family: "Marcellus SC", serif; font-weight: 400;
    color: var(--brand-blue); line-height: 1; white-space: nowrap;
  }

  .card--front .brand { left: 20px; top: 122px; width: 310px; }
  .card--front .brand__mark { width: 100px; height: 100px; margin-bottom: 16px; }
  .card--front .brand__name { font-size: 30px; }

  .contact {
    position: absolute; left: 392px; top: 212px;
    font-family: "Marcellus SC", serif; color: var(--ink);
    font-size: 16px; line-height: 21px; letter-spacing: .3px;
    list-style: none;
  }
  .contact__web { margin-top: 21px; }

  .card--back .brand { left: 0; top: 108px; width: 100%; }
  .card--back .brand__mark { width: 124px; height: 124px; margin-bottom: 20px; }
  .card--back .brand__name { font-size: 44px; }
</style>
</head>
<body>
<main class="stage">

  <section class="card card--front" aria-label="Business card front">
    <header class="title-band">
      <p class="title-band__name">Tobias Wendell</p>
      <p class="title-band__role">President</p>
    </header>

    <div class="brand">
      <span class="brand__mark"></span>
      <span class="brand__name">Pelverhook LLC</span>
    </div>

    <ul class="contact">
      <li>482 Orchard Crest Road</li>
      <li>Dunmore Falls, NJ 07934-2718</li>
      <li>P: 555.310.4829</li>
      <li>C: 555.310.7163</li>
      <li>F: 555.310.4829</li>
      <li>E: tobias.wendell@mailvexo.com</li>
      <li class="contact__web">www.pelverhook.com</li>
    </ul>
  </section>

  <section class="card card--back" aria-label="Business card back">
    <div class="brand">
      <span class="brand__mark"></span>
      <span class="brand__name">Pelverhook LLC</span>
    </div>
  </section>

</main>
</body>
</html>
```